Beauty Therapy Web Design

I need a web page design for a small beauty therapy clinic, the owner is currently the only beauty therapist working there.
We require the following pages:
Home
About
Treatments
Nails
Courses
Contact
I will attach the clinics business card, treatment menu and signage so that you get a feeling for the branding colours etc.
This is the first website for the beauty therapist, she would like to attract new clients and also tourists that come in on the cruise ships. The thing that sets her apart from other clinics is that she welcomes texting for appointments.
I have selected refundable because I have never done this before so I don't know what to expect, I have the full intention of going through with it as long as I get a good design.
Feel free to ask for further information
Reason: Project extended as I am away for work and am unable to meet with the owner.
Target Market(s)
Females 18 to 50
Industry/Entity Type
Business
Look and feel
Each slider illustrates characteristics of the customer's brand and the style your logo design should communicate.

```html
<!DOCTYPE html>
<html lang="en">
<head>
<meta charset="utf-8">
<title>Velora Beauty Therapy – Treatments</title>
<link rel="stylesheet" href="https://fonts.googleapis.com/css2?family=Arimo:wght@400;700&family=Tinos:wght@400;700&display=swap">
<style>
  :root {
    --purple: #7a62ae;
    --purple-deep: #6a519e;
    --purple-light: #8d76bd;
    --gold: #c9a84c;
    --gold-pale: #f1e4a9;
    --gold-line: #d8bf6a;
    --paper: #fdfcf7;
    --lavender: #e1dde7;
    --ink: #111111;
    --tab-active: #d2691e;
    --frame-dark: #2c2c4e;
    --white: #ffffff;
  }
  * { box-sizing: border-box; margin: 0; padding: 0; }
  html, body { width: 1200px; height: 775px; overflow: hidden; }
  body {
    position: relative;
    font-family: "Arimo", Arial, sans-serif;
    color: var(--ink);
    background:
      radial-gradient(ellipse 140px 110px at 320px 0, rgba(255,255,255,.35), transparent 70%),
      radial-gradient(ellipse 140px 110px at 880px 0, rgba(255,255,255,.35), transparent 70%),
      radial-gradient(ellipse 120px 90px at 600px 0, rgba(255,255,255,.25), transparent 70%),
      linear-gradient(var(--purple-light), var(--purple) 35%, var(--purple));
  }

  /* Brand header */
  .brand { position: absolute; left: 0; top: 0; width: 1200px; text-align: center; font-family: "Tinos", "Times New Roman", serif; color: var(--gold); }
  .brand-name { position: absolute; left: 0; width: 100%; top: 2px; font-size: 72px; line-height: 80px; font-weight: 400; }
  .brand-sub { position: absolute; left: 0; width: 100%; top: 92px; font-size: 54px; line-height: 60px; font-weight: 400; }
  .brand-rule { position: absolute; left: 400px; top: 164px; width: 410px; height: 5px; background: var(--gold); }
  .brand-phone { position: absolute; left: 0; width: 100%; top: 186px; font-size: 26px; line-height: 32px; font-weight: 700; }

  /* Main page frame */
  .page { position: absolute; left: 104px; top: 227px; width: 1004px; height: 529px; border: 2px solid var(--gold-line); border-radius: 6px; background: var(--purple); overflow: hidden; }

  .tabs { position: absolute; left: 0; top: 0; width: 100%; height: 44px; border-bottom: 3px solid var(--gold-line); }
  .tab { position: absolute; top: 14px; height: 30px; background: var(--gold-pale); border: 1px solid var(--gold-line); border-bottom: none; border-radius: 5px 5px 0 0; font-size: 14px; line-height: 29px; text-align: center; color: #3a3a3a; }
  .tab.is-active { background: var(--white); color: var(--tab-active); top: 12px; height: 35px; }

  .col-left { position: absolute; left: 1px; top: 47px; width: 328px; height: 443px; background: var(--paper); }
  .col-right { position: absolute; left: 329px; top: 47px; width: 671px; height: 443px; background: var(--lavender); }

  /* Price list */
  .price-card { position: absolute; left: 12px; top: 38px; width: 303px; height: 305px; background: linear-gradient(135deg, #3b3a66, var(--frame-dark) 50%, #4a4a72); padding: 14px 16px; }
  .price-card-inner { width: 100%; height: 100%; background: var(--white); padding: 6px 12px; font-family: "Tinos", "Times New Roman", serif; }
  .price-title { font-size: 19px; font-weight: 700; line-height: 24px; text-decoration: underline; margin-bottom: 3px; }
  .price-row { display: flex; font-size: 14.5px; line-height: 21.3px; }
  .price-row .item { width: 193px; }

  /* Hero photographs */
  .hero { position: absolute; left: 28px; top: 19px; width: 614px; height: 308px; border: 3px solid var(--gold-line); display: flex; }
  .hero-photo-waxing { width: 222px; height: 100%; background: linear-gradient(135deg, #f3eeea, #d9b9a5 55%, #c09a86); }
  .hero-photo-spa { flex: 1; height: 100%; background: linear-gradient(120deg, #6b4a34, #d7ae90 45%, #efe3d6 75%, #f7f1ea); }

  .appointment { position: absolute; left: 0; width: 100%; text-align: center; font-weight: 700; }
  .appointment-lead { top: 353px; font-size: 18.5px; }
  .appointment-text { top: 386px; font-size: 18.5px; }
  .appointment-link { top: 419px; font-size: 17px; }

  .footer { position: absolute; left: 0; top: 490px; width: 100%; height: 37px; background: var(--purple-deep); color: var(--white); text-align: center; font-size: 11.5px; line-height: 13px; padding-top: 5px; }
</style>
</head>
<body>
  <header class="brand">
    <div class="brand-name">Velora</div>
    <div class="brand-sub">Beauty Therapy</div>
    <div class="brand-rule"></div>
    <div class="brand-phone">Phone: 07 555 0142</div>
  </header>

  <main class="page">
    <nav class="tabs">
      <div class="tab" style="left:5px;width:67px">Home</div>
      <div class="tab" style="left:80px;width:88px">About Us</div>
      <div class="tab is-active" style="left:176px;width:97px">Treatments</div>
      <div class="tab" style="left:281px;width:62px">Nails</div>
      <div class="tab" style="left:351px;width:85px">Courses</div>
      <div class="tab" style="left:444px;width:95px">Contact Us</div>
    </nav>

    <section class="col-left">
      <div class="price-card">
        <div class="price-card-inner">
          <div class="price-title">Waxing</div>
          <div class="price-row"><span class="item">Full Leg</span><span>$50.00</span></div>
          <div class="price-row"><span class="item">Half Leg</span><span>$25.00</span></div>
          <div class="price-row"><span class="item">Thigh</span><span>$25.00</span></div>
          <div class="price-row"><span class="item">Bikini</span><span>$18.00</span></div>
          <div class="price-row"><span class="item">Brazilian (monthly)</span><span>$40.00</span></div>
          <div class="price-row"><span class="item">Under Arm</span><span>$15.00</span></div>
          <div class="price-row"><span class="item">Arm</span><span>$25.00</span></div>
          <div class="price-row"><span class="item">Lip</span><span>$12.00</span></div>
          <div class="price-row"><span class="item">Lip &amp; Chin</span><span>$20.00</span></div>
          <div class="price-row"><span class="item">Lip &amp; Brow Shape</span><span>$20.00</span></div>
        </div>
      </div>
    </section>

    <section class="col-right">
      <div class="hero">
        <div class="hero-photo-waxing" role="img" aria-label="Photo of a therapist applying a waxing strip"></div>
        <div class="hero-photo-spa" role="img" aria-label="Photo of a client relaxing during a chocolate body treatment with candles"></div>
      </div>
      <p class="appointment appointment-lead">Make An Appointment Today</p>
      <p class="appointment appointment-text">By Texting <span style="font-weight:400">021 555 0187</span></p>
      <p class="appointment appointment-link">Appointment</p>
    </section>

    <footer class="footer">
      <div>Home | About Us |Treatments | Nails | Courses | Contact Us</div>
      <div>Copyright © 2011. All Rights Reserved.</div>
    </footer>
  </main>
</body>
</html>
```